BRAVOLK PROMOTION GROUP Website

Looking for a website design that clearly and powerfully portrays our unique and effective indoor advertising billboards in our network.

Our TeenyPanels, LargoPanels and TitanFlags are strategically placed in high traffic areas of restaurants, pubs, nightclubs, fitness clubs, colleges and universities, and sports arenas.

Bravolk Promotion Group is our new name. Our current site is www.plorvex.ca with our focus now being entirely on our Out-of-Home media. New website address will be www.bravolkpromotion.ca

We need the following sections:

HOME
PRODUCTS (Drop down menu)
-TeenyPanels
-LargoPanels
-TitanFlags
NETWORKS (Drop down menu)
-Resto-Bar
-Sports
-Campus
EFFECTIVENESS
CAMPAIGNS *This page will show numerous ad campaigns and could be a slide show (see www.plorvex.ca/QJPV_campaigns.html )
BECOME A PARTNER
CONTACT

Please include social media functions on the homepage such as chirpnet/visagebook/workloop

We will be supplying content and photos as required.

Our plan is to have you submit the homepage design to start with, and then we can start judging which styles we like the best and can start narrowing our list. As a second round, we would like to ask the "finalists" to submit a second page (another section of the website) and to see how consistent you are in terms of the look and feel you proposed for the homepage.

Attached is our new logo.

We may require you to upload the final website for us.

Websites that are in similar industry are:
www.trelmuk.com
www.quasplen.com

Industry/Entity Type

Advertising

Requirements
Must have
• Our network offers advertising solutions that feature: Guaranteed Readership,100% Gender Specific, Frequency, and Captive Audience. Purchasing advertising space in our network are small to medium business owners and advertising agencies booking on behalf of their clients.

Site must be professional and modern looking.
Nice to have
• Moving banner or slide show of some type.

```html
<!DOCTYPE html>
<html lang="en">
<head>
<meta charset="utf-8">
<title>Bravolk Promotion Group</title>
<link rel="stylesheet" href="https://fonts.googleapis.com/css2?family=Open+Sans:wght@400;600;700&display=swap">
<style>
:root{
  --page:#e4e4e4;
  --header-top:#ffffff;
  --header-bottom:#f0f0f0;
  --text:#737373;
  --heading:#5c5c5c;
  --link:#2a62b0;
  --brand:#2d6bb8;
  --nav-bg:#eef2f5;
  --nav-border:#c9d3da;
  --green:#5e8f1f;
  --green-dark:#3f6612;
  --search-green:#6cc35a;
  --white:#ffffff;
}
*{box-sizing:border-box;margin:0;padding:0}
html,body{width:1023px;height:1200px;overflow:hidden}
body{background:var(--page);font-family:"Open Sans",Verdana,sans-serif;color:var(--text);position:relative}
.site-header{position:absolute;left:0;top:0;width:1023px;height:193px;background:linear-gradient(var(--header-top),var(--header-bottom));border-bottom:2px solid #d6d6d6;z-index:1}
.brand{position:absolute;left:65px;top:62px;display:flex;align-items:center;gap:12px}
.brand-mark{width:36px;height:36px;background:var(--brand)}
.brand-name{font-size:26px;font-weight:700;color:var(--brand);line-height:1.1;width:230px}
.search{position:absolute;left:672px;top:27px;width:286px;height:52px;border-radius:26px;border:2px solid #bfe0dc;background:#f7fbfb;display:flex;align-items:center;padding:0 9px;gap:10px}
.search-field{width:170px;height:32px;border:1px solid #c8c8c8;border-radius:4px 0 0 4px;background:#fff;font-size:12px;font-style:italic;color:#a8a8a8;padding:7px 10px}
.search-btn{width:84px;height:32px;border-radius:6px;background:linear-gradient(#86d574,var(--search-green));color:#234d1a;font-size:13px;font-weight:600;text-align:center;line-height:32px}
.main-nav{position:absolute;left:384px;top:117px;width:574px;height:54px;background:var(--nav-bg);border:1px solid var(--nav-border);display:flex;align-items:center;justify-content:space-between;padding:0 12px 0 16px;font-size:11px;color:#7a7a7a;white-space:nowrap}
.main-nav .current{background:var(--white);height:53px;line-height:53px;padding:0 10px;margin:0 -10px;align-self:flex-start}
.dropdown{position:absolute;left:444px;top:170px;width:168px;height:108px;background:var(--white);padding:20px 14px 0;font-size:11px;color:#888;line-height:28.5px;z-index:5;letter-spacing:.2px}
.slider{position:absolute;left:65px;top:207px;width:893px;height:462px;background:var(--white)}
.slide-photo{position:absolute;left:11px;top:11px;width:872px;height:441px;background:linear-gradient(180deg,#b9bcbe 0%,#8d9aa8 45%,#4d6e9a 62%,#8b8b88 88%,#a6a39a 100%)}
.slide-dots{position:absolute;left:402px;top:417px;width:90px;height:28px;border-radius:8px;background:rgba(60,55,45,.75);display:flex;align-items:center;justify-content:center;gap:8px}
.slide-dots i{width:12px;height:12px;border-radius:50%;background:#d9d4c6}
.slide-dots i:first-child{background:#8a8576;border:2px solid #d9d4c6}
.arrow{position:absolute;top:409px;width:52px;height:52px;border-radius:50%;background:var(--white);box-shadow:0 1px 4px rgba(0,0,0,.2);display:flex;align-items:center;justify-content:center}
.arrow-prev{left:39px}.arrow-next{left:931px}
.welcome{position:absolute;left:65px;top:683px;width:893px}
h2{font-size:21px;font-weight:400;color:var(--heading);letter-spacing:.5px;line-height:28px}
.welcome p{font-size:10.8px;line-height:14.4px;margin-top:8px;letter-spacing:.35px}
.read-more{position:absolute;right:0;top:145px;color:var(--link);font-size:13px}
.services-title{position:absolute;left:65px;top:856px;word-spacing:5px}
.service{position:absolute;top:905px;width:229px;height:188px;background:var(--white);border:1px solid #cfcfcf}
.service .photo{position:absolute;left:4px;top:4px;right:4px;bottom:4px}
.service .tag{position:absolute;left:-26px;top:3px;height:40px;width:180px;background:linear-gradient(#75a82c,var(--green));color:#fff;font-size:12px;line-height:40px;padding-left:44px;clip-path:polygon(0 0,150px 0,180px 50%,150px 100%,0 100%)}
.service .fold{position:absolute;left:-26px;top:43px;width:0;height:0;border-top:10px solid var(--green-dark);border-left:26px solid transparent}
.site-footer{position:absolute;left:0;top:1152px;width:1023px;text-align:center;font-size:11.5px}
.footer-links{color:#777;letter-spacing:.3px}
.copyright{margin-top:7px;color:#666;font-size:12px;margin-right:56px}
.copyright a{color:var(--link);text-decoration:none}
.social{position:absolute;left:798px;top:1157px;display:flex;gap:8px}
.social span{width:36px;height:36px;border-radius:50%;background:#5b7fb0;color:#fff;font-size:7px;display:flex;align-items:center;justify-content:center;text-align:center;line-height:1.1}
</style>
</head>
<body>
<header class="site-header">
  <div class="brand"><span class="brand-mark"></span><span class="brand-name">Bravolk Promotion Group</span></div>
  <div class="search"><div class="search-field">Type here</div><div class="search-btn">Search</div></div>
  <nav class="main-nav">
    <span>Home</span><span class="current">Products</span><span>Networks</span><span>Effectiveness</span><span>Become A Partner</span><span>Campaigns</span><span>Contacts</span>
  </nav>
</header>

<section class="slider">
  <div class="slide-photo" role="img" aria-label="Large indoor billboard wall of blue and white advertising panels above a stadium entrance"></div>
  <div class="slide-dots"><i></i><i></i><i></i><i></i></div>
</section>
<div class="dropdown"><div>TEENYPANELS</div><div>LARGOPANELS</div><div>TITANFLAGS</div></div>
<div class="arrow arrow-prev"><svg width="16" height="14" viewBox="0 0 16 14"><path d="M7 1 1 7l6 6M15 1 9 7l6 6" fill="none" stroke="#333" stroke-width="2.6"/></svg></div>
<div class="arrow arrow-next"><svg width="16" height="14" viewBox="0 0 16 14"><path d="M1 1l6 6-6 6M9 1l6 6-6 6" fill="none" stroke="#333" stroke-width="2.6"/></svg></div>

<section class="welcome">
  <h2>WELCOME</h2>
  <p>Lorem ipsum dolor sit amet, consectetuer adipiscing elit. Aenean commodo ligula eget dolor. Aenean massa. Cum sociis natoque penatibus et magnis dis parturient montes, nascetur ridiculus mus. Donec quam felis, ultricies nec, pellentesque eu, pretium quis, sem. Nulla consequat massa quis enim. Donec pede justo, fringilla vel, aliquet nec, vulputate eget, arcu. In enim justo, rhoncus ut, imperdiet a, venenatis vitae, justo. Nullam dictum felis eu pede mollis pretium. Integer tincidunt. Cras dapibus. Vivamus elementum semper nisi. Aenean vulputate eleifend tellus. Aenean leo ligula, porttitor eu, consequat vitae, eleifend ac, enim. Aliquam lorem ante, dapibus in. do ligula eget dolor. Aenean massa. Cum sociis natoque penatibus et magnis dis parturient montes, nascetur ridiculus mus. Donec quam felis, ultricies nec, pellentesque eu, pretium quis, sem. Nulla consequat massa quis enim. Donec pede justo, fringilla vel, aliquet nec, vulputate e do ligula eget dolor. Aenean massa. Cum sociis natoque penatibus et magnis dis parturient montes, nascetur ridiculus mus.</p>
  <span class="read-more">Read more!</span>
</section>

<h2 class="services-title">OUR SERVICES</h2>
<div class="service" style="left:113px">
  <div class="photo" role="img" aria-label="Framed small indoor panels mounted on a tiled washroom wall" style="background:linear-gradient(90deg,#e6e2da 0%,#cfcac0 45%,#2d3a5e 55%,#2f5aa8 100%)"></div>
  <div class="tag">TEENYPANEL</div><div class="fold"></div>
</div>
<div class="service" style="left:403px">
  <div class="photo" role="img" aria-label="Large backlit indoor panel showing an athlete advert" style="background:linear-gradient(90deg,#4a5b8a 0%,#6f7a63 40%,#4f6a3c 70%,#23283d 100%)"></div>
  <div class="tag">LARGOPANEL</div><div class="fold"></div>
</div>
<div class="service" style="left:694px">
  <div class="photo" role="img" aria-label="Stadium scoreboard with advertising boards above a running track" style="background:linear-gradient(180deg,#c9d3de 0%,#a9b3bd 40%,#3b3f46 58%,#7d8b6f 76%,#b0483a 100%)"></div>
  <div class="tag">OTHER BOARD</div><div class="fold"></div>
</div>

<footer class="site-footer">
  <div class="footer-links">HOME | ABOUT US | NETWORK | CONTACTS</div>
  <div class="copyright">Copyright © 2012 <a href="#">bravolk promotion group</a>. All rights reserved</div>
</footer>
<div class="social"><span>visage<br>book</span><span>work<br>loop</span><span>orbit<br>sphere</span><span>chirp<br>net</span></div>
</body>
</html>
```